BEACON CABS

Taxi card design

Need changes very slow in replying to my messages.

Target Market(s)

Customers

Industry/Entity Type

Taxi

Contact Information for Business Card

See previous design

Font styles to use
Sans Serif

Colors
A7469A
B969AE
D3A5CF
EDDBEB
F8F0F9
6B429C
8869AF
B7A5CE
E3DAEB
F3F0F8

Requirements
Nice to have
• We are in the business of looking after people, not just driving vehicles front
Should not have
• Front number 01632 480 480 needs to big big

```html
<!DOCTYPE html>
<html lang="en">
<head>
<meta charset="utf-8">
<title>Beacon Cabs – Business Card</title>
<link href="https://fonts.googleapis.com/css2?family=Montserrat:wght@500;700;800&display=swap" rel="stylesheet">
<style>
  :root{
    --magenta:#b62d8c;
    --magenta-deep:#98287f;
    --plum:#6e2474;
    --indigo:#4a2672;
    --service-text:#8a2580;
    --ink:#161616;
    --paper:#ffffff;
  }
  *{box-sizing:border-box;margin:0;padding:0}
  html,body{width:1200px;height:1200px;overflow:hidden;background:var(--paper)}
  body{position:relative;font-family:"Montserrat",Arial,sans-serif;color:var(--ink)}
  .card{position:absolute;left:276px;width:645px;height:431px;box-shadow:6px 8px 14px rgba(0,0,0,.22);overflow:hidden}
  .card--front{top:145px;background:var(--paper)}
  .card--back{top:630px;height:461px;background:linear-gradient(180deg,var(--magenta-deep),var(--plum))}

  .brand{position:absolute;left:0;right:0;text-align:center}
  .brand__name{display:inline-flex;align-items:center;gap:12px;font-weight:800;letter-spacing:-1px;line-height:1}
  .brand__mark{display:inline-block;background:var(--magenta)}
  .brand__meta{position:absolute;font-weight:700;white-space:nowrap}

  .card--front .brand{top:62px}
  .card--front .brand__name{font-size:52px;color:var(--ink)}
  .card--front .brand__mark{width:26px;height:26px}
  .card--front .est{left:142px;top:150px;font-size:15px}
  .card--front .hours{left:396px;top:151px;font-size:20px}

  .hotline{position:absolute;left:0;top:185px;width:100%;height:55px;display:flex;align-items:center;justify-content:center;gap:14px;
    background:linear-gradient(90deg,var(--magenta),#8a2c88 55%,var(--indigo));color:#fff;font-weight:700;font-size:42px;letter-spacing:.5px}
  .hotline svg{width:44px;height:44px}

  .pills{position:absolute;top:264px;left:46px;display:flex;gap:8px}
  .pill{width:179px;height:22px;border-radius:8px;display:flex;align-items:center;justify-content:center;gap:4px;
    background:linear-gradient(90deg,var(--magenta),var(--indigo));color:#fff;font-weight:700;font-size:17px}
  .pill svg{width:16px;height:16px}

  .contact{position:absolute;top:314px;font-size:16px;font-weight:500;line-height:21px}
  .contact--info{left:51px}
  .contact--address{left:386px}

  .card--back .brand{top:105px}
  .card--back .brand__name{font-size:64px;color:#fff}
  .card--back .brand__mark{width:30px;height:30px;background:#fff}
  .card--back .est{left:82px;top:182px;font-size:20px;color:#fff}
  .card--back .hours{left:418px;top:198px;font-size:27px;color:#fff}

  .decor-car{position:absolute;right:18px;top:80px;width:30px;height:300px;border-radius:14px;
    background:linear-gradient(180deg,rgba(255,255,255,.05),rgba(255,255,255,.14),rgba(255,255,255,.05))}

  .services{position:absolute;left:0;top:257px;list-style:none}
  .service{width:360px;height:39px;margin-bottom:12px;background:#fff;border-radius:0 8px 8px 0;display:flex;align-items:center;
    color:var(--service-text);font-weight:700;font-size:24px;letter-spacing:.3px}
  .service svg{width:34px;height:26px;margin:0 25px 0 22px;fill:var(--service-text)}
</style>
</head>
<body>

<section class="card card--front">
  <div class="brand">
    <span class="brand__name"><span class="brand__mark"></span>BEACON CABS</span>
  </div>
  <span class="brand__meta est">Established since 1986</span>
  <span class="brand__meta hours">24/7 Service</span>

  <div class="hotline">
    <svg viewBox="0 0 24 24" fill="none" stroke="#fff" stroke-width="1.6" stroke-linecap="round"><path d="M6 3l3 4-2 2c1 3 4 6 7 7l2-2 4 3-2 3c-7 0-14-7-14-14z"/><path d="M14 3a7 7 0 0 1 7 7M14 6a4 4 0 0 1 4 4"/></svg>
    <span>01632 480 480</span>
  </div>

  <div class="pills">
    <div class="pill"><svg viewBox="0 0 24 24" fill="none" stroke="#fff" stroke-width="2"><path d="M6 3l3 4-2 2c1 3 4 6 7 7l2-2 4 3-2 3c-7 0-14-7-14-14z"/></svg>01632 480 480</div>
    <div class="pill"><svg viewBox="0 0 24 24" fill="none" stroke="#fff" stroke-width="2"><path d="M6 3l3 4-2 2c1 3 4 6 7 7l2-2 4 3-2 3c-7 0-14-7-14-14z"/></svg>01632 480 480</div>
    <div class="pill"><svg viewBox="0 0 24 24" fill="none" stroke="#fff" stroke-width="2"><path d="M6 3l3 4-2 2c1 3 4 6 7 7l2-2 4 3-2 3c-7 0-14-7-14-14z"/></svg>01632 480 480</div>
  </div>

  <p class="contact contact--info">Freephone: 0800 555 0 199<br>Email: hello@beaconcabs.example<br>Website: www.beaconcabs.example</p>
  <p class="contact contact--address">St Marys Parish Hall<br>Market Row<br>Linwell<br>LN4 7QT</p>
</section>

<section class="card card--back">
  <div class="brand">
    <span class="brand__name"><span class="brand__mark"></span>BEACON CABS</span>
  </div>
  <span class="brand__meta est">Established since 1986</span>
  <span class="brand__meta hours">24/7 Service</span>

  <div class="decor-car" role="img" aria-label="Faint outline of a car in side view"></div>

  <ul class="services">
    <li class="service"><svg viewBox="0 0 24 24"><path d="M21 3l-6 5-9-3-2 2 7 4-4 4-3-1-1 1 3 2 2 3 1-1-1-3 4-4 4 7 2-2-3-9 5-6z"/></svg>AIRPORT TRANSFERS</li>
    <li class="service"><svg viewBox="0 0 24 24"><path d="M6 2h12a2 2 0 0 1 2 2v14h-1v3h-3v-3H8v3H5v-3H4V4a2 2 0 0 1 2-2zm0 3v6h12V5zm1 9a1.3 1.3 0 1 0 0 2.6A1.3 1.3 0 0 0 7 14zm10 0a1.3 1.3 0 1 0 0 2.6A1.3 1.3 0 0 0 17 14z"/></svg>MINIBUSES</li>
    <li class="service"><svg viewBox="0 0 32 20"><path d="M2 8l5-6h20a3 3 0 0 1 3 3v10h-3a3 3 0 0 0-6 0H11a3 3 0 0 0-6 0H2zm7-4-3 4h5V4zm4 0v4h5V4zm7 0v4h5V4zM8 14a2 2 0 1 1 0 4 2 2 0 0 1 0-4zm16 0a2 2 0 1 1 0 4 2 2 0 0 1 0-4z"/></svg>SCHOOL TRANSPORT</li>
  </ul>
</section>

</body>
</html>
```